依頼詳細
当社製品の取り扱い店舗や代理店様に向けて、事務所移転の案内はがきをだしますが、当社製品ブランドのブランドイメージをさらに向上させるようなスタイリッシュなハガキデザインを依頼いたします。
ハガキサイズは通常のハガキサイズ

社名:株式会社ミルテカ
住所 旧 東京都江東区有明5-3-9 theLOFTA 412
新 東京都江東区有明5-3-9 theLOFTA 418

412号室から418号室へ移転。

電話:03-5812-9076
FAX : 03-5812-9077
URL : www.miruteka.jp
MAIL : support@miruteka.jp
記載項目
会社名・新住所(旧住所)・電話番号・ファックス番号
希望イメージ
• シンプル
複雑
• 単色
カラフル
• 暗い
明るい
• 日常
高級
• 遊び心
厳粛
• 未来的
伝統的
• 女性的
男性的
希望する色
グレー系、ブランドイメージカラーは黒系ですが、インパクトのある色彩を使って頂くのも楽しいかと思います。
納品ファイル
• 高解像度JPG (.jpg)
• イラストレーター形式 (.ai)
補足説明
ロゴデータを添付します。
依頼公開後の追記内容
■ 選んだ理由

当社のブランディングにあった洗練されたデザインがとても気に入りました。

■ 提案者全員のお礼・コメント

この度は大変多くのご提案を頂きまして誠に有り難うございます。
今後も様々なグラフィックデザインをFiverdoで募集しますので、今回当選にならなかった方々も是非またご提案を頂けましたら幸いと存じます。

```html
<!DOCTYPE html>
<html lang="ja">
<head>
<meta charset="utf-8">
<title>事務所移転のお知らせ</title>
<link rel="stylesheet" href="https://fonts.googleapis.com/css2?family=Noto+Sans+JP:wght@400;500;700&display=swap">
<style>
  :root {
    --paper: #ffffff;
    --card: #000000;
    --ink-light: #ffffff;
    --ink-dark: #111111;
    --accent: #d7262c;
    --rule: #bfbfbf;
  }
  html, body {
    margin: 0;
    padding: 0;
    width: 849px;
    height: 1200px;
    overflow: hidden;
    background: var(--paper);
    font-family: "Noto Sans JP", sans-serif;
  }
  .postcard {
    position: absolute;
    left: 156px;
    top: 54px;
    width: 552px;
    height: 1102px;
    background: var(--card);
    color: var(--ink-light);
  }
  .brand {
    position: absolute;
    left: 330px;
    top: 240px;
    display: flex;
    align-items: center;
    gap: 12px;
  }
  .brand-dot {
    width: 54px;
    height: 54px;
    border-radius: 50%;
    background: var(--accent);
  }
  .brand-name {
    color: var(--accent);
    font-weight: 700;
    font-size: 24px;
    line-height: 1.05;
    letter-spacing: 0.02em;
  }
  .headline {
    position: absolute;
    left: 16px;
    top: 366px;
    width: 510px;
    height: 56px;
  }
  .headline svg { position: absolute; left: 0; top: 0; }
  .headline-text {
    position: absolute;
    left: 28px;
    top: 0;
    height: 56px;
    line-height: 56px;
    color: var(--ink-dark);
    font-size: 27px;
    font-weight: 500;
    letter-spacing: 0.04em;
  }
  .message {
    position: absolute;
    left: 28px;
    top: 452px;
    width: 500px;
    margin: 0;
    font-size: 15px;
    line-height: 31px;
  }
  .message p { margin: 0; }
  .contact {
    position: absolute;
    left: 26px;
    top: 824px;
    margin: 0;
    font-size: 17px;
    line-height: 27px;
  }
  .contact p { margin: 0; white-space: nowrap; }
  .contact .company { margin-bottom: 4px; }
  .contact .label { display: inline-block; width: 26px; }
  .new-mark {
    display: inline-block;
    width: 14px;
    height: 14px;
    border-radius: 50%;
    background: var(--accent);
    margin: 0 12px 0 0;
    vertical-align: -1px;
  }
  .room-new { color: var(--accent); }
  .new-tag { vertical-align: -3px; margin-left: 6px; }
</style>
</head>
<body>
  <main class="postcard">
    <div class="brand">
      <span class="brand-dot"></span>
      <span class="brand-name">NOVA<br>SHIELD</span>
    </div>

    <div class="headline">
      <svg width="510" height="56" viewBox="0 0 510 56">
        <line x1="400" y1="28" x2="510" y2="28" stroke="var(--rule)" stroke-width="2"/>
        <rect x="2" y="2" width="398" height="52" rx="10" fill="var(--ink-light)"/>
      </svg>
      <h1 class="headline-text" style="margin:0;font-weight:500">事務所移転のお知らせ</h1>
    </div>

    <div class="message">
      <p>このたび弊社株式会社ミルテカは業務拡張に伴い、</p>
      <p>本社事務所を下記に移転することになりました。</p>
      <p>新事務所は同ビル内の418号室となります。</p>
      <p>よりアクティブな営業活動の拠点となるものと存じます。</p>
      <p>これを機に、皆様の信頼にお応えできるよう倍旧の努力をしてまいる</p>
      <p>所存でございます。</p>
      <p>今後とも一層のご支援を賜りますようお願い申し上げます。</p>
    </div>

    <div class="contact">
      <p class="company">株式会社ミルテカ(ノヴァシールド)</p>
      <p><span class="label">旧</span>東京都江東区有明5-3-9 theLOFTA 412</p>
      <p><span class="new-mark"></span>東京都江東区有明5-3-9 theLOFTA <span class="room-new">418</span><svg class="new-tag" width="30" height="18" viewBox="0 0 30 18"><path d="M1 1 H22 L29 9 L22 17 H1 Z" fill="var(--ink-light)"/></svg></p>
      <p>TEL : 03-5812-9076</p>
      <p>FAX : 03-5812-9077</p>
      <p>URL : www.miruteka.jp</p>
      <p>MAIL : support@miruteka.jp</p>
    </div>
  </main>
</body>
</html>
```